Coral Bay Condo project in Ibiza Spain, qualifies for immigrant investor Visa

We need a website for Coral Bay Condo project in Ibiza Spain.
The target audience will be investors from China, Russia, South America, and other countries where people are interested in obtaining visas to reside or travel freely in EU countries.

Crestmoor Holdings is offering a limited number of luxury condominium residences “Los Tarales” in Ibiza, Spain which qualifies buyers to immediate residency visas for Spain

The GOLDEN VISA is available to Los Tarales purchasers who invest a minimum of 500,000€. The visa can be renewed and full citizenship can become available after five years.

The website will be English first, but later translated to Chinese, Spanish, and possibly Russian.

A PDF Summary of the Crestmoor Holdings offering is attached (look and feel is NOT consistent with what we want in the website.

The look and feel of this website is attractive to us as an example:

http://www.velbrook-resorts.example/

Also attached is a brochure from another company talking about the Golden Visa Opportunity. We will use some of the same messaging in our copy.

We are looking for someone who will help us with the copywriting as well as the web design.

The website must be fully optimized for key word/google search etc.

We will consider other than wordpress if we can be assured that optimization is effective.

We will need to have a number of PDF Downloads available for the users of the site also.

We need to edit the copy from time - to - time, this will be an important consideration also.

```html
<!DOCTYPE html>
<html lang="en">
<head>
<meta charset="utf-8">
<title>Coral Bay Condo</title>
<link rel="stylesheet" href="https://fonts.googleapis.com/css2?family=Rokkitt:wght@400;500;700&display=swap">
<style>
:root{
  --orange:#f47920;
  --ink:#3d3d3d;
  --text:#555;
  --rule:#bdbdbd;
  --nav-top:#fbfbfb;
  --nav-bot:#e9e9e9;
  --footer-dark:#3f3f3f;
  --blue:#1597d8;
}
*{box-sizing:border-box;margin:0;padding:0}
html,body{width:693px;height:1200px;overflow:hidden;background:#fff}
body{font-family:"Rokkitt",Georgia,serif;color:var(--text);position:relative}
.abs{position:absolute}
.orange{color:var(--orange)}

/* header */
.brand{left:54px;top:20px;display:flex;align-items:center;gap:10px}
.brand-dot{width:22px;height:22px;border-radius:50%;background:var(--orange)}
.brand-name{color:var(--orange);font-weight:700;font-size:24px;line-height:23px}
.lang{left:401px;top:21px;font-size:9px;color:#222;display:flex;align-items:center;gap:5px}
.flag{width:13px;height:8px;display:inline-block}
.search{left:531px;top:16px;width:107px;height:21px;border-radius:11px;background:#f0f0f0;font-size:8px;color:#777;padding:6px 10px;font-style:italic}
.search svg{position:absolute;right:6px;top:4px}
.contact-line{left:401px;top:57px;font-size:9px;color:#222;display:flex;gap:12px;align-items:center;white-space:nowrap}
.contact-line span.g{color:#999}

/* nav */
.nav{left:0;top:86px;width:693px;height:32px;background:linear-gradient(var(--nav-top),var(--nav-bot));border-top:1px solid #ddd;border-bottom:1px solid #ddd}
.nav ul{list-style:none;display:flex;margin-left:66px;height:100%}
.nav li{padding:0 9px;font-size:11.5px;line-height:31px;color:#555;border-right:1px solid #d6d6d6;letter-spacing:.2px}
.nav li.active{background:var(--orange);color:#fff;border-right:none}

/* hero */
.hero{left:0;top:118px;width:693px;height:282px;background:linear-gradient(90deg,#eceff2,#c9ccd0 40%,#b9bcc0 60%,#e6e8ea)}
.hero-caption{left:240px;top:250px;width:214px;height:56px;background:rgba(60,60,60,.72);color:#fff;text-align:center;font-size:15.5px;line-height:20px;padding-top:8px;letter-spacing:.3px}

/* section headings */
.heading{width:693px;text-align:center;font-size:19px;font-weight:500;color:var(--ink);letter-spacing:.3px}
.divider{display:flex;gap:3px;justify-content:center;width:693px}
.divider i{display:block;height:2px;background:var(--rule);width:36px}
.divider i.c{background:var(--orange);width:13px}
.intro{left:82px;top:461px;width:529px;text-align:center;font-size:8.6px;line-height:13px;color:#444}
.hr{left:54px;top:537px;width:585px;height:1px;background:#ddd}

/* services */
.card{top:610px;width:181px}
.card-img{position:absolute;top:32px;left:0;width:181px;height:100px;border-top:2px solid #555}
.card.featured .card-img{border-top-color:var(--orange)}
.card-badge{position:absolute;left:58px;top:0;width:64px;height:64px;border-radius:50%;background:#fff;border:2px solid #555;display:flex;align-items:center;justify-content:center}
.card.featured .card-badge{background:var(--orange);border:3px solid #fff;box-shadow:0 0 0 2px var(--orange)}
.card h3{position:absolute;top:143px;width:181px;text-align:center;font-size:10px;font-weight:500;color:#333;letter-spacing:.2px}
.card.featured h3{color:var(--orange)}
.card p{position:absolute;top:164px;width:181px;text-align:center;font-size:8.5px;line-height:13px;color:#666}
.card-rule{position:absolute;top:221px;width:181px;height:2px;background:#555}
.card.featured .card-rule{background:var(--orange)}
.card-arrow{position:absolute;top:212px;left:81px;width:20px;height:20px;border-radius:50%;background:#555}
.card.featured .card-arrow{background:var(--orange)}
.card-arrow svg{position:absolute;left:6px;top:5px}

/* news + testimonials */
.block-title{font-size:19px;font-weight:500;color:var(--ink);letter-spacing:.3px}
.left-divider{display:flex;gap:3px}
.left-divider i{display:block;height:2px;background:var(--rule);width:36px}
.left-divider i.c{background:var(--orange);width:13px}
.news{top:908px;width:110px}
.news .date{font-size:8.5px;color:#222}
.news h4{font-size:9.5px;font-weight:400;color:var(--orange);margin-top:9px}
.news p{font-size:8px;line-height:12px;color:#666;margin-top:6px}
.btn{background:var(--orange);color:#fff;font-size:8px;padding:4px 6px;display:inline-block}
.testimonial{left:420px;top:907px;width:220px;font-size:8.3px;line-height:13px;color:#666}
.testimonial .who{margin-top:6px;color:#333}
.testimonial .who b{font-weight:400;color:var(--blue)}

/* footer */
.footer{left:0;top:1016px;width:693px;height:149px;background:var(--orange)}
.footer h5{position:absolute;color:#fff;font-size:13px;font-weight:500;letter-spacing:.3px}
.field{position:absolute;background:#fff;border-radius:4px;font-size:8.5px;color:#777;padding:7px 11px}
.submit{position:absolute;left:376px;top:72px;width:63px;height:58px;border-radius:4px;background:linear-gradient(135deg,#1eb3ef,#0b7fc7);color:#fff;font-weight:700;font-size:11px;display:flex;align-items:center;justify-content:center;letter-spacing:.3px}
.visit{position:absolute;left:474px;color:#fff;font-size:8.5px;line-height:12px;display:flex;gap:8px;align-items:flex-start;white-space:nowrap}
.bottom{left:0;top:1165px;width:693px;height:35px;background:var(--footer-dark);font-size:8.2px;color:#aaa}
.bottom .links{position:absolute;left:54px;top:13px}
.bottom .links .on{color:var(--orange)}
.bottom .legal{position:absolute;right:56px;top:13px}
</style>
</head>
<body>

<header>
  <div class="abs brand">
    <span class="brand-dot"></span>
    <div class="brand-name">Coral Bay<br>Condo</div>
  </div>
  <div class="abs lang">Lanugaue
    <span class="flag" style="background:#1f3d8a"></span>
    <span class="flag" style="background:#de2910"></span>
    <span class="flag" style="background:linear-gradient(#c60b1e 25%,#ffc400 25% 75%,#c60b1e 75%)"></span>
    <span class="flag" style="background:linear-gradient(#fff 33%,#0039a6 33% 66%,#d52b1e 66%)"></span>
  </div>
  <div class="abs search">Search
    <svg width="12" height="12" viewBox="0 0 12 12" fill="none" stroke="#f47920" stroke-width="1.6"><circle cx="5" cy="5" r="3.6"/><path d="M7.6 7.6 11 11"/></svg>
  </div>
  <div class="abs contact-line">
    <span><svg width="9" height="10" viewBox="0 0 10 10"><path d="M2 1l2 2-1 1.5c.5 1.2 1.3 2 2.5 2.5L7 6l2 2-1.5 1.5C4 9 1 6 .5 2z" fill="#f47920"/></svg> Call us Now: <span class="g">555 010 4400</span></span>
    <span><svg width="11" height="8" viewBox="0 0 11 8"><rect width="11" height="8" fill="#f47920"/><path d="M0 0l5.5 4.5L11 0" stroke="#fff" fill="none"/></svg>&nbsp; info@coralbaycondo.example</span>
  </div>
</header>

<nav class="abs nav">
  <ul>
    <li class="active">HOME</li><li>ABOUT</li><li>COUNTRY</li><li>BUSINESS OPPORTUNITY</li><li>IMM IGRATION</li><li>NEWS</li><li style="border-right:none">CONTACT</li>
  </ul>
</nav>

<section class="abs hero" role="img" aria-label="Photo of four smiling business people giving thumbs up in a bright office"></section>
<div class="abs hero-caption">GET YOUR GOLDEN VISA<br>GET WAY TO SPAIN</div>

<section class="welcome">
  <h1 class="abs heading" style="top:418px">WELCOME TO <span class="orange">CORAL BAY CONDO</span></h1>
  <div class="abs divider" style="top:448px"><i></i><i class="c"></i><i></i></div>
  <p class="abs intro">Lorem ipsum dolor sit amet, consectetur adipiscing elit. Praesent sed libero at eros ullamcorper posuere. Nam odio nibh, ultrices sit amet ultricies id, feugiat vel ligula. Praesent fermentum, tellus vel tempus placerat, risus neque tristique libero, id finibus est lacus in augue. Donec justo lacus, porta eu nunc ut, tristique convallis nulla. Integer consequat, enim eget malesuada vulputate, arcu eros luctus turpis,</p>
  <div class="abs hr"></div>
</section>

<section class="services">
  <h2 class="abs heading" style="top:561px">OUR &nbsp;<span class="orange">SERVICES</span></h2>
  <div class="abs divider" style="top:591px"><i></i><i class="c"></i><i></i></div>

  <article class="abs card featured" style="left:54px">
    <div class="card-img" role="img" aria-label="Photo of a business team meeting around a table" style="background:linear-gradient(135deg,#dfe3e8,#8a97a8)"></div>
    <div class="card-badge"><svg width="30" height="30" viewBox="0 0 30 30" fill="none" stroke="#fff" stroke-width="1.6"><circle cx="15" cy="13" r="10"/><path d="M5 13h20M15 3c-4 4-4 16 0 20M15 3c4 4 4 16 0 20"/><circle cx="15" cy="18" r="2.5" fill="#fff"/><path d="M11 28c0-4 8-4 8 0" fill="#fff"/></svg></div>
    <h3>INVESTOR AND GOLDEN VISA</h3>
    <p>Lorem ipsum dolor sit amet, consect-etur adipiscing elit. Praesent sed libero at eros ullamcorper posuer nibh...</p>
    <div class="card-rule"></div>
    <div class="card-arrow"><svg width="9" height="10" viewBox="0 0 9 10" fill="none" stroke="#fff" stroke-width="2"><path d="M2 1l4 4-4 4"/></svg></div>
  </article>

  <article class="abs card" style="left:256px">
    <div class="card-img" role="img" aria-label="Photo of a presenter speaking to colleagues in a meeting room" style="background:linear-gradient(135deg,#eef0f2,#8d939a)"></div>
    <div class="card-badge"><svg width="30" height="30" viewBox="0 0 30 30" fill="#444"><circle cx="8" cy="7" r="3"/><path d="M5 11h6v8H9v8H7v-8H5z"/><path d="M12 12l9-5v12l-9-4z"/><path d="M23 10h4M23 13h4M23 16h4" stroke="#444" stroke-width="1.2"/></svg></div>
    <h3>2014 SPANISH GOVT.VISA</h3>
    <p>Lorem ipsum dolor sit amet, consect-etur adipiscing elit. Praesent sed libero at eros ullamcorper posueio nibh...</p>
    <div class="card-rule"></div>
    <div class="card-arrow"><svg width="9" height="10" viewBox="0 0 9 10" fill="none" stroke="#fff" stroke-width="2"><path d="M2 1l4 4-4 4"/></svg></div>
  </article>

  <article class="abs card" style="left:458px">
    <div class="card-img" role="img" aria-label="Photo of colleagues planning at a whiteboard" style="background:linear-gradient(135deg,#e6ebf0,#9aa5b2)"></div>
    <div class="card-badge"><svg width="30" height="30" viewBox="0 0 30 30" fill="#444"><circle cx="15" cy="7" r="3"/><path d="M11 14a4 4 0 0 1 8 0z"/><circle cx="7" cy="18" r="2.5"/><path d="M3 24a4 4 0 0 1 8 0z"/><circle cx="23" cy="18" r="2.5"/><path d="M19 24a4 4 0 0 1 8 0z"/><path d="M6 12a9 9 0 0 1 4-5M24 12a9 9 0 0 0-4-5M11 27h8" stroke="#444" stroke-width="1.4" fill="none"/></svg></div>
    <h3>IMMIGRANT INVETTOR PROGRAM</h3>
    <p>Lorem ipsum dolor sit amet, consect-etur adipiscing elit. Praesent sed libero at eros ullamcorper posuere nibh...</p>
    <div class="card-rule"></div>
    <div class="card-arrow"><svg width="9" height="10" viewBox="0 0 9 10" fill="none" stroke="#fff" stroke-width="2"><path d="M2 1l4 4-4 4"/></svg></div>
  </article>
</section>

<section class="latest-news">
  <h2 class="abs block-title" style="left:54px;top:863px">LATEST <span class="orange">NEWS</span></h2>
  <div class="abs left-divider" style="left:54px;top:892px"><i></i><i class="c"></i><i></i></div>
  <article class="abs news" style="left:54px"><div class="date">29. 09. 2014</div><h4>News Coverage And</h4><p>Lorem ipsum dolor sitmet, consectetur adipiscing elit.</p></article>
  <article class="abs news" style="left:174px"><div class="date">29. 09. 2014</div><h4>Vivamus turpis justo</h4><p>Lorem ipsum dolor sitmet, consectetur adipiscing elit.</p></article>
  <article class="abs news" style="left:294px"><div class="date">29. 09. 2014</div><h4>News Coverage And</h4><p>Lorem ipsum dolor sitmet, consectetur adipiscing elit.</p></article>
  <span class="abs btn" style="left:54px;top:973px">More News</span>
</section>

<section class="testimonials">
  <h2 class="abs block-title" style="left:420px;top:863px">CLIENTS <span class="orange">TESTIMONIALS</span></h2>
  <div class="abs left-divider" style="left:420px;top:892px"><i></i><i class="c"></i><i></i></div>
  <blockquote class="abs testimonial">BLorem ipsum dolor sit amet, consectetur adipiscinge. Praesent sed libero at eros ullamcorper posuere. Namo nibh, ultrices sit amet ultricies id, feugiat vel ligula....
    <div class="who"><b>- Lorem Ispum</b> - Director company Pty Ltd.</div>
  </blockquote>
  <span class="abs btn" style="left:419px;top:973px">More News</span>
</section>

<footer class="abs footer">
  <h5 style="left:54px;top:12px">CONTACT US</h5>
  <div class="field" style="left:54px;top:38px;width:188px;height:25px">Your Name:</div>
  <div class="field" style="left:251px;top:38px;width:188px;height:25px">Email:</div>
  <div class="field" style="left:54px;top:72px;width:313px;height:58px">Comments:</div>
  <div class="submit">SUBMIT</div>

  <h5 style="left:474px;top:12px">VISIT TO SOLANA</h5>
  <div class="visit" style="top:39px"><svg width="16" height="16" viewBox="0 0 16 16" fill="#fff"><rect x="7" y="1" width="2" height="15"/><path d="M1 3h11l2 2-2 2H1zM15 8H4L2 10l2 2h11z"/></svg><span>PO Box: 9101, lorem Ispum,<br>Dolar sit , Spain 3844</span></div>
  <div class="visit" style="top:79px"><svg width="14" height="14" viewBox="0 0 10 10"><path d="M2 1l2 2-1 1.5c.5 1.2 1.3 2 2.5 2.5L7 6l2 2-1.5 1.5C4 9 1 6 .5 2z" fill="#fff"/></svg><span style="padding-top:2px;font-weight:700">555 010 4400</span></div>
  <div class="visit" style="top:116px"><svg width="16" height="12" viewBox="0 0 16 12"><rect width="16" height="12" fill="#fff"/><path d="M0 0l8 6 8-6M0 12l6-6M16 12l-6-6" stroke="#f47920" fill="none"/></svg><span>contact@coralbaycondo.example</span></div>
</footer>

<div class="abs bottom">
  <div class="links"><span class="on">Home</span> &nbsp;/&nbsp; About &nbsp;/&nbsp; Country &nbsp;/&nbsp; Business Oppurtinity &nbsp;/&nbsp; News / &nbsp;Contact</div>
  <div class="legal">© 2014 <span class="orange">coralbay condo</span>. &nbsp;Privacy Policy | Terms of Use</div>
</div>

</body>
</html>
```